Little Ones Can Soar
Brochure
onescansoar.org
I have a logo that was created by brand (business cards) mark maven and a web site that was designed by pixel sage, I am interested in intergrating those designs into two or tri fold business brochure. Your company has all the records that are needed
Corporate, businesses, retailers, Individuals and people of all walks of life. (prospects of give)
Need a brochure not expensive to print. What would be you suggestion as to the type of brochure needed?

```html
<!DOCTYPE html>
<html lang="en">
<head>
<meta charset="utf-8">
<title>Little Ones Can Soar INC. – Brochure</title>
<link href="https://fonts.googleapis.com/css2?family=Arimo:wght@400;700&display=swap" rel="stylesheet">
<style>
  :root{
    --header-grey:#5c5c5c;
    --band-grey:#6a6a6a;
    --band-light:#8c8c8c;
    --band-dark:#474747;
    --ink:#333333;
    --white:#ffffff;
    --photo-light:#b9b9b9;
    --photo-dark:#6f6f6f;
  }
  *{margin:0;padding:0;box-sizing:border-box}
  html,body{width:1200px;height:850px;overflow:hidden;background:var(--white)}
  body{font-family:"Arimo",Arial,sans-serif;color:var(--ink);position:relative}
  .sheet{position:relative;width:1200px;height:850px}

  .about{position:absolute;left:0;top:0;width:1200px;height:206px;background:var(--header-grey);color:var(--white)}
  .about__photo{position:absolute;left:0;top:0;width:156px;height:206px;background:linear-gradient(160deg,var(--photo-light),var(--photo-dark))}
  .about__title{position:absolute;left:170px;top:8px;font-size:38px;font-weight:400;letter-spacing:.3px;white-space:nowrap}
  .about__body{position:absolute;left:170px;top:64px;width:1010px;font-size:12.5px;line-height:1.3}
  .about__body p{margin-bottom:9px}

  .goals{position:absolute;left:0;top:206px;width:1200px;height:156px;background:var(--band-dark)}
  .goals__label{position:absolute;left:0;top:0;width:470px;height:156px}
  .goals__heading{position:absolute;left:12px;top:58px;font-size:27px;font-weight:400;color:var(--white);white-space:nowrap}
  .goals__list{position:absolute;left:475px;top:22px;width:700px;list-style:none;color:var(--white);font-size:14px;line-height:1.2}
  .goals__list li{margin-bottom:2px}

  .volunteers__photo{position:absolute;left:0;top:368px;width:380px;height:190px;background:linear-gradient(180deg,var(--photo-light),var(--photo-dark))}
  .col-head{font-size:25px;font-weight:400;color:var(--ink)}
  .volunteers{position:absolute;left:16px;top:566px;width:370px;font-size:13px;line-height:1.3}
  .volunteers p{margin:8px 0 10px}
  .roles{display:grid;grid-template-columns:1fr 1fr;column-gap:14px;font-size:13px;line-height:1.3}

  .founder{position:absolute;left:398px;top:368px;width:272px;font-size:13px;line-height:1.3}
  .founder p{margin-bottom:12px}
  .founder__photo{position:absolute;left:684px;top:420px;width:120px;height:96px;background:linear-gradient(160deg,var(--photo-light),var(--band-dark))}
  .founder__name{position:absolute;left:690px;top:522px;font-size:13px}
  .founder__cont{position:absolute;left:398px;top:560px;width:410px;font-size:13px;line-height:1.3}
  .founder__cont p{margin-bottom:12px}
  .partners{position:absolute;left:398px;top:660px;width:400px;font-size:13px;line-height:1.3}
  .partners p{margin-top:6px}

  .membership{position:absolute;left:840px;top:368px;width:345px;font-size:13px;line-height:1.3}
  .membership p{margin-bottom:12px}
</style>
</head>
<body>
<main class="sheet">
  <header class="about">
    <div class="about__photo" role="img" aria-label="Photo of smiling children"></div>
    <h1 class="about__title">About us at Little Ones Can Soar INC.</h1>
    <div class="about__body">
      <p>Little Ones Can Soar Inc. mission is to enrich kids learning by providing the essential tools to succeed. The experiences the kids will have while participating in the company's programs will assist them in making their transition from grade level to grade level more smoothly. The resources will allow them to develop their skill sets that will be transferable in advanced grades.</p>
      <p>Kids should be taught how to communicate, speak and interact with peers appropriately. They should be provided various materials, games and activities to be motivated to learn in the areas of language, vocabulary, reading, mathematics, science, computers and social behaviors (discipline). Underserved kids need gifts of school supplies, backpacks, uniforms, and other essential tools to function in school.</p>
      <p>The kid demographic market has changed in the urban areas. Kids need help. Parents are losing their jobs and cannot provide for their kids basic educational necessities.</p>
    </div>
  </header>

  <section class="goals">
    <svg class="goals__label" viewBox="0 0 470 156" aria-hidden="true">
      <polygon points="0,0 430,0 466,78 430,156 0,156" fill="#8c8c8c"/>
    </svg>
    <h2 class="goals__heading">Our Goals &nbsp;as an Organization are</h2>
    <ul class="goals__list">
      <li>Understand urban school problems</li>
      <li>Adapt to education model for communities to achieve</li>
      <li>Create partnership and strategic alliances to improve the learning process in communities</li>
      <li>Underserved kids need gifts of school supplies, backpacks, uniforms, and other essential tools to function in school</li>
    </ul>
  </section>

  <div class="volunteers__photo" role="img" aria-label="Photo of a group of young volunteers"></div>
  <section class="volunteers">
    <h2 class="col-head">Volunteers</h2>
    <p>Please take this opportunity to get involved, by volunteering your talent and skills to a worthwhile cause.</p>
    <p>Volunteers are the fiber of our organization. If you are interested in becoming a volunteer and want to learn more about us, just forward us an e-mail.</p>
    <div class="roles">
      <span>Grant Writers<br>"Little Ones Can Soar"<br>Members Photographers</span>
      <span>Planners of fundraisers<br>Social Workers<br>Web Designers</span>
    </div>
  </section>

  <section class="founder">
    <p>Dana is the founder of the organization since its inception, a native of Jacksonville Fl.</p>
    <p>Dana was a territory manager for Harwell Tobacco company for nine</p>
    <p>Dana is the founder of the organization since its inception, a native of Jacksonville Fl.</p>
  </section>
  <div class="founder__photo" role="img" aria-label="Portrait of the founder"></div>
  <div class="founder__name">Dana R. Whitfield</div>
  <section class="founder__cont">
    <p>maintaining a 4/million yr. territory in central New Jersey.</p>
    <p>Dana worked twenty-two years as an operational auditor for Coastline Transit corporation. Developed audit reports outlining any irregularities and recommended improvements on compliance issues.</p>
  </section>
  <section class="partners">
    <h2 class="col-head">Partners Commited</h2>
    <p>Membership with kid "Little Ones Can Soar Inc." is a tax exempt organization.</p>
  </section>

  <section class="membership">
    <p>Membership allows special privileges in joining an elite organization. The important benefit is knowing that your contribution has a two (2) fold feature.</p>
    <p>Helping underserved kids by providing the tools necessary to achieve by donating to this worthwhile cause is tax deductible Contributions are tax deductible under 501(c)3 federal tax law.</p>
    <p>The organization will provide written acknowledgement to you for your generous contribution above $250.00 or more.</p>
    <p>The organization has created a company's logo, with a pledge of $50.00 you will receive a free company's cap for your support. Shipment is paid by the person.</p>
    <p>In regards to your $50.00 pledge, the total of $37.55 is tax deductible under the federal tax guidelines.</p>
  </section>
</main>
</body>
</html>
```